***PLASTIC*** Business Card Design

1 sided business card design
The card will be screen printed on plastic, so colour and fonts must be strong.

Must use the colours in the logo eps attached (Black/Ivory/White). Other colour(s) can be added.

Four (4) examples of how the logo can be printed are included in the logo eps attached.

The business card should highlight the logo. The card will be given to architects, interior designers and builders. It should look sophisticated but also innovative.

Do not cover the whole card with colour as it is important than some of the frosted plastic card is visible.

Be creative.

Target Market(s)

architects, interior designers and builders and wealthy home owners

Industry/Entity Type

Plastic

Requirements
Must have
• Must use the colours in the logo eps attached (Black/Ivory/White). Other colour(s) can be added if necessary.

The font is Square721 ExBT but has been a little thickened. It is not essential that you use this font. The name should be a stronger version of the font than other details.

The card will be printed on PVC - see http://www.voltrap.com.au/pricelistbcardsplastic.php

Final artwork must be print ready. You must use the printing spec at http://www.voltrap.com.au/2011%20PVC-TW.pdf

The actual details to be typeset ono the card are:

Dorian Welch

Mobile: 0412 806133
email: info@halcoworks.com.au
www.halcoworks.com.au

PO Box 53, Altona, Vic 3018

Plastering | Rendering | Cornicing

```html
<!DOCTYPE html>
<html lang="en">
<head>
<meta charset="utf-8">
<title>Halco Works – Plastic Business Card</title>
<link rel="stylesheet" href="https://fonts.googleapis.com/css2?family=Source+Sans+3:wght@400;600;700&display=swap">
<style>
  :root {
    --backdrop: #5e0b0b;
    --card-black: #000000;
    --frost: rgba(226, 221, 218, 0.62);
    --frost-edge: rgba(255, 255, 255, 0.6);
    --white: #ffffff;
    --ink: #141414;
    --ink-soft: #262626;
    --icon-cut: #d8d4d0;
  }
  * { box-sizing: border-box; margin: 0; padding: 0; }
  html, body {
    width: 1200px;
    height: 900px;
    overflow: hidden;
    background: var(--backdrop);
    font-family: "Source Sans 3", "Myriad Pro", Arial, sans-serif;
  }
  .stage {
    position: relative;
    width: 1200px;
    height: 900px;
    display: flex;
    align-items: center;
    justify-content: center;
  }
  .card {
    position: relative;
    width: 900px;
    height: 576px;
    border-radius: 40px;
    overflow: hidden;
    background: var(--frost);
    border: 2px solid var(--frost-edge);
    box-shadow: 0 18px 40px rgba(0, 0, 0, 0.35);
  }
  .card__header {
    height: 296px;
    background: var(--card-black);
    display: flex;
    align-items: center;
    justify-content: center;
    gap: 26px;
  }
  .brand__mark {
    width: 46px;
    height: 46px;
    background: var(--white);
  }
  .brand__name {
    font-weight: 700;
    font-size: 92px;
    letter-spacing: 10px;
    color: var(--white);
    text-transform: uppercase;
    line-height: 1;
  }
  .card__body {
    position: relative;
    height: 280px;
  }
  .contact-list {
    position: absolute;
    left: 32px;
    top: 34px;
    list-style: none;
  }
  .contact-list__item {
    display: flex;
    align-items: center;
    gap: 22px;
    height: 34px;
    font-size: 23px;
    color: var(--ink);
  }
  .contact-list__item strong { font-weight: 700; }
  .icon {
    width: 30px;
    height: 26px;
    flex: none;
  }
  .postal {
    position: absolute;
    left: 32px;
    top: 176px;
    display: flex;
    align-items: center;
    gap: 22px;
    font-size: 24px;
    font-weight: 700;
    color: var(--ink);
  }
  .postal .icon { height: 40px; }
  .holder-name {
    position: absolute;
    right: 52px;
    top: 70px;
    font-size: 38px;
    font-weight: 700;
    color: var(--ink-soft);
    letter-spacing: 0.5px;
  }
</style>
</head>
<body>
<main class="stage">
  <article class="card">
    <header class="card__header">
      <span class="brand__mark"></span>
      <span class="brand__name">Halco Works</span>
    </header>

    <section class="card__body">
      <ul class="contact-list">
        <li class="contact-list__item">
          <svg class="icon" viewBox="0 0 30 26" aria-hidden="true">
            <path d="M3 8 Q15 0 27 8 L27 11 L21 11 L20 8 L10 8 L9 11 L3 11 Z" fill="#141414"/>
            <rect x="7" y="13" width="16" height="11" rx="2" fill="#141414"/>
          </svg>
          <span>0412 806133</span>
        </li>
        <li class="contact-list__item">
          <svg class="icon" viewBox="0 0 30 26" aria-hidden="true">
            <rect x="2" y="4" width="26" height="18" fill="#141414"/>
            <path d="M2 4 L15 15 L28 4" fill="none" stroke="#d8d4d0" stroke-width="2"/>
          </svg>
          <span><strong>info</strong>@halcoworks.com.au</span>
        </li>
        <li class="contact-list__item">
          <svg class="icon" viewBox="0 0 30 26" aria-hidden="true">
            <circle cx="15" cy="13" r="10" fill="none" stroke="#141414" stroke-width="3"/>
            <path d="M5 13 H25 M15 3 Q9 13 15 23 M15 3 Q21 13 15 23" fill="none" stroke="#141414" stroke-width="2"/>
          </svg>
          <span>www.<strong>halcoworks</strong>.com.au</span>
        </li>
      </ul>

      <div class="postal">
        <svg class="icon" viewBox="0 0 30 40" aria-hidden="true">
          <path d="M15 2 C8 2 3 7 3 14 C3 23 15 38 15 38 C15 38 27 23 27 14 C27 7 22 2 15 2 Z" fill="#141414"/>
          <circle cx="15" cy="14" r="5" fill="#d8d4d0"/>
        </svg>
        <span>PO Box 53, Brayfield, Vic 3061</span>
      </div>

      <p class="holder-name">Dorian Welch</p>
    </section>
  </article>
</main>
</body>
</html>
```